High-end law practice specializing in closely held business succession planning and complex estates

Solo practitioner whose practice specializes in high-net worth, complex estate planning needs muliple versions of letterhead black and white, please. Letterhead should incorporate slogan, "Guarding your family legacy is my lifelong calling," for one and "Complex Estate Planning"; third with no slogan. All for The Law Office of Marguerite Elaine Haskett, PC, 418 Cedar Hollow Ln., Ashford Mills, Maryland 23847, Tel. 757-481-5390 Fax tbd email: marguerite@mehcounsel.example; Marguerite Elaine Haskett, Esq., principal, licensed in VA, NY, DC
Updates

Project Deadline Extended
Reason: My internet service went down and I can only view designs on my smart phone -- it's just too hard to review. So sorry! Working with my ISP now. Please be patient!

Target Market(s)

High net worth clients with complex estate planning needs, family businesses, family farmers, family foresters -- people with unique estate/succession planning needs who need a specialist who understands them.

Industry/Entity Type

Business

Font styles to use
Script

Requirements
Must have
• A high-end look and feel, connoting trustworthiness, special knowledge, and expertise.

```html
<!DOCTYPE html>
<html lang="en">
<head>
<meta charset="utf-8">
<title>Letterhead – The Law Office of Marguerite Elaine Haskett, PC</title>
<link href="https://fonts.googleapis.com/css2?family=Cinzel:wght@400;500&family=Open+Sans:wght@400&display=swap" rel="stylesheet">
<style>
  :root {
    --backdrop: #d6d6d6;
    --paper: #ffffff;
    --ink: #111111;
    --band: #0d0d0d;
    --strip: #5e5e5e;
    --faint: #ececec;
    --footer-text: #e6e6e6;
    --divider: #cfcfcf;
  }
  * { margin: 0; padding: 0; box-sizing: border-box; }
  html, body { width: 1200px; height: 900px; overflow: hidden; }
  body { background: var(--backdrop); position: relative; }

  .letterhead {
    position: absolute;
    left: 301px; top: 70px;
    width: 603px; height: 765px;
    background: var(--paper);
    box-shadow: 0 2px 8px rgba(0,0,0,0.12);
  }

  .masthead {
    position: absolute;
    top: 20px; left: 0; width: 100%;
    text-align: center;
    color: var(--ink);
    font-family: 'Cinzel', serif;
  }
  .masthead-initials {
    font-size: 40px;
    font-weight: 500;
    letter-spacing: 2px;
    line-height: 1;
    margin-top: 22px;
  }
  .masthead-rule {
    width: 88px; height: 4px;
    background: var(--ink);
    margin: 8px auto 0;
  }
  .masthead-office {
    font-size: 10px;
    letter-spacing: 0.5px;
    margin-top: 22px;
    line-height: 1.2;
  }
  .masthead-name {
    font-size: 12.5px;
    letter-spacing: 0.4px;
    line-height: 1.2;
  }

  .watermark {
    position: absolute;
    left: 0; width: 100%;
    top: 380px;
    text-align: center;
    font-family: 'Cinzel', serif;
    font-size: 120px;
    font-weight: 400;
    color: var(--faint);
    line-height: 1;
    letter-spacing: 4px;
  }

  .contact-band {
    position: absolute;
    left: 0; top: 700px;
    width: 100%; height: 48px;
    background: var(--band);
    display: flex;
    justify-content: center;
    align-items: center;
    gap: 14px;
    font-family: 'Open Sans', sans-serif;
    font-size: 8.5px;
    color: var(--footer-text);
    line-height: 1.25;
  }
  .contact-group { display: flex; flex-direction: column; gap: 1px; font-style: normal; }
  .contact-line { display: flex; align-items: center; gap: 4px; white-space: nowrap; }
  .contact-line svg { width: 8px; height: 8px; fill: var(--footer-text); flex: none; }
  .contact-divider { width: 1px; height: 32px; background: var(--divider); }

  .slogan-strip {
    position: absolute;
    left: 0; top: 748px;
    width: 100%; height: 17px;
    background: var(--strip);
    text-align: center;
    font-family: 'Cinzel', serif;
    font-size: 11px;
    color: #ffffff;
    line-height: 17px;
    letter-spacing: 0.4px;
  }
</style>
</head>
<body>
  <main class="letterhead">
    <header class="masthead">
      <div class="masthead-initials">MEH</div>
      <div class="masthead-rule"></div>
      <p class="masthead-office">THE LAW OFFICE OF</p>
      <p class="masthead-name">MARGUERITE ELAINE HASKETT, PC</p>
    </header>

    <div class="watermark" aria-hidden="true">MEH</div>

    <footer>
      <div class="contact-band">
        <div class="contact-group">
          <span class="contact-line">
            <svg viewBox="0 0 10 10" aria-label="Phone"><rect width="10" height="10" rx="1.5"/><path d="M3 2.2l1 1.6-.6.7c.4.9 1.1 1.6 2 2l.7-.6 1.6 1-.5 1.1C4.9 7.9 2.1 5.1 2 2.7z" fill="#0d0d0d"/></svg>
            757-481-5390
          </span>
          <span class="contact-line">
            <svg viewBox="0 0 10 10" aria-label="Fax"><rect x="2.5" y="0.5" width="5" height="3"/><rect x="0.5" y="3.5" width="9" height="4" rx="1"/><rect x="2.5" y="6" width="5" height="3.5"/></svg>
            757-481-5390
          </span>
        </div>
        <span class="contact-divider"></span>
        <div class="contact-group">
          <span class="contact-line">
            <svg viewBox="0 0 10 10" aria-label="Email"><rect x="0.5" y="2" width="9" height="6"/><path d="M0.5 2L5 5.5 9.5 2" fill="none" stroke="#0d0d0d" stroke-width="1"/></svg>
            marguerite@mehcounsel.example
          </span>
          <span class="contact-line">
            <svg viewBox="0 0 10 10" aria-label="Website"><circle cx="5" cy="5" r="4.5"/><path d="M0.5 5h9M5 0.5c-2 2.5-2 6.5 0 9M5 0.5c2 2.5 2 6.5 0 9" fill="none" stroke="#0d0d0d" stroke-width="0.7"/></svg>
            www.mehcounsel.example
          </span>
        </div>
        <span class="contact-divider"></span>
        <address class="contact-group">
          <span>PC, 418 Cedar Hollow Ln., Ashford Mills,</span>
          <span>Maryland 23847</span>
        </address>
      </div>
      <p class="slogan-strip">Guarding your family legacy is my lifelong calling</p>
    </footer>
  </main>
</body>
</html>
```